Health care finance company startup website design

This design brief is for Ledger Nest, a small start-up company dealing with an online health care (initially dental targeted with plans for medical market) financial suite of tools. My business partners and I are looking to have a website developed for our business model.

We have developed a professional logo and would like it incorporated into the site. We are open to modifications on the logo if needed to accomplish the right design.

Our concept is a clean, simple design with a professional polish and very up-to-date web presence. The functionality of the site is simple yet powerful and we would like it’s design to complement that (including anticipated css3/html5 effects for an added dimension of UI polish).

We would like to see a design mockup of the functional elements of our site as our home page. We would also be very interested to see how your design would flow into the other pages such as search for a loan, create a payment plan, make a payment, sign in, registration, contact us and learn more.

Regarding Functional Elements:

-Simplicity is king.

-The three main functions of the site are the focus. They will operate via a series of API’s to webservices on the back-end, making the front end field focused, though we hope to have it feel friendly and simple.
-Search for a loan
-Create a payment plan
-Make a payment

Other functions of the site include:

-Sign in module
-We plan to support Kindlebook Link, Vornix Authentication and TrellisKey so incorporating design for those options is a plus.

-Registration module
-Two service levels clients can register for, loans only or loans & payments
-The registration process should be divided into sections with navigation back and forth until a confirmation final screen with pdf generations and remaining “to-do items” listed.
-The registration information will be saved in our database and also auto-populate fields for PDF’s that will be generated from templates.
-The registration will send a confirmation email and support TrellisKey, Vornix Authentication and Kindlebook Link, so designs should take these programmatic features into account.

-Contact us
-This will emphasize digital forms of communication (email and form submitted contact request).

-Learn more
-Explanations/faqs/tutorials
-This will contain video demonstrations/screencasts of key functions of website features

Regarding Design Elements:
-We want to be “wow’d” and don’t mind a surprise that redefines what we thought we liked regarding design.
-The following examples indicate some of the color schemes we like and design elements we hope to incorporate.
-We also recognize there is no substitute for creativity and originality.

Favorite Website Design Examples:

http://www.joginmarla.example/
HD backgrounds are a plus.
These colors are great.
The bright splashes of blue, red and orange combined with black in these shades.
A predominant background of whitesmoke or beige.

https://tillbrook.example/
The HD backgrounds are sharp.
The look is very clean (though it has a slight Quince computers imitation).
The left to right “scrolling” is preferable to vertical scrolling.
Very pleasing to the eye.

http://www.quarryfilmworks.example/
Again, use of bright, vibrant HD graphics is exceptional.
The left to right scrolling navigation is slick and likely how we would like our services to flow.

http://latest.wanderpelmark.example/
Love the look, feel and concepts in this site’s design
Especially colors and “photography” elements.
Updates

We've seen a few common themes in various designs submitted so far and want to add a few suggestions as we enter the final week of our design contest.

We do not want any photos of healthcare professionals or close-ups of people (families or couples or individuals).  Although we are a health care company we don't want to fall into a cliche feel for our site.  Instead we would like either objects or abstract images that have depth and are high definition, spanning from edge to edge of the width of the screen. 

We prefer shades of grey for the base color scheme with highlights of bright colors.  Please refer to the examples on the brief and use those as the best guide of what we want.  Even SketchGuild's color scheme is closer to what we want than some of the submissions, so please take note of the "shades of grey" with splashes of bright accent colors.

We love the horizontal navigation bar like that seen in the quarry filmworks site and anticipate our final product using a similar transition between the functions of the site.

Good luck to you all.  We are still looking for that WOW factor and hoping to see something original, that breaks the traditional mold and has a feel like the examples posted.

```html
<!DOCTYPE html>
<html lang="en">
<head>
<meta charset="utf-8">
<title>Ledger Nest — Easy Loan Process</title>
<link rel="stylesheet" href="https://fonts.googleapis.com/css2?family=Signika:wght@300;400;600&family=Yanone+Kaffeesatz:wght@300;600&family=Arimo:wght@400;700&display=swap">
<style>
:root{
  --navy:#1d3f6e;
  --navy-dark:#143158;
  --blue:#3e6298;
  --brand-blue:#1f4a85;
  --orange:#f7941d;
  --orange-deep:#ee6a0c;
  --sky:#d8ecfa;
  --ink:#2b2b2b;
  --footer:#2d2d2d;
  --footer-bar:#1f1f1f;
  --gold:#e5c36a;
  --white:#fff;
}
*{box-sizing:border-box;margin:0;padding:0}
html,body{width:1200px;height:1029px;overflow:hidden}
body{position:relative;font-family:"Arimo",Arial,sans-serif;color:var(--ink);background:var(--sky)}

/* header */
.site-header{position:absolute;left:0;top:0;width:1200px;height:110px;
  background:linear-gradient(160deg,#e6f3fc 0%,#c9e4f7 55%,#b4d8f2 100%)}
.brand{position:absolute;left:207px;top:31px;display:flex;align-items:center;gap:12px}
.brand-mark{width:47px;height:47px;background:var(--brand-blue);border-radius:6px}
.brand-name{font-family:"Signika",sans-serif;font-weight:300;font-size:34px;color:var(--brand-blue);letter-spacing:1px;white-space:nowrap}
.account{position:absolute;right:189px;top:11px;display:flex;align-items:center;gap:14px;font-size:11px;white-space:nowrap}
.account .register{color:#222}
.account .sign-in{background:linear-gradient(#ffb23c,var(--orange-deep));color:#3a1a00;padding:5px 9px;border-radius:12px;font-weight:700;font-size:10.5px}
.social-connect{position:absolute;left:846px;top:43px;width:165px;height:20px;background:linear-gradient(#3b5b92,#29467a);color:#fff;font-family:"Signika",sans-serif;font-weight:400;font-size:12px;line-height:20px;white-space:nowrap;display:flex;align-items:center;gap:8px;padding-left:5px;border-radius:2px;overflow:hidden}
.social-connect .sq{flex:none;width:12px;height:12px;background:#fff;opacity:.85}
.header-social{position:absolute;left:921px;top:77px;display:flex;gap:5px}
.header-social i{width:19px;height:19px;background:#8d9aa6;border-radius:3px;display:block}

/* nav */
.main-nav{position:absolute;left:0;top:110px;width:1200px;height:44px;background:linear-gradient(#2c5c96,var(--navy-dark))}
.main-nav a{position:absolute;top:0;height:44px;line-height:44px;color:#fff;font-size:11px;text-decoration:none;white-space:nowrap}
.main-nav a.active{background:var(--orange);color:#222;padding:0 10px}
.main-nav .sep{position:absolute;top:10px;width:1px;height:24px;background:rgba(255,255,255,.18)}

/* hero */
.hero{position:absolute;left:0;top:154px;width:1200px;height:660px;
  background:radial-gradient(ellipse at 15% 40%,#ffffff 0%,#e6f2fb 35%,#bddcf3 75%,#a9d0ef 100%)}
.hero-city{position:absolute;left:620px;top:0;width:580px;height:640px;
  background:linear-gradient(200deg,#6ebf3f 0%,#c9d3dc 30%,#d9dfe6 55%,#c37b5a 75%,#7ac04a 100%);
  opacity:.85;border-bottom-left-radius:260px}
.search-panel{position:absolute;left:180px;top:38px;width:468px;height:273px;background:rgba(255,255,255,.94);border-radius:5px;box-shadow:0 2px 8px rgba(0,0,0,.18)}
.search-panel .eyebrow{position:absolute;left:15px;top:12px;font-family:"Signika",sans-serif;font-weight:300;font-size:18px;color:var(--orange-deep);white-space:nowrap}
.search-panel h1{position:absolute;left:14px;top:32px;font-family:"Signika",sans-serif;font-weight:300;font-size:38px;color:#1d3450;letter-spacing:-.5px;white-space:nowrap}
.search-panel p{position:absolute;left:15px;top:82px;width:440px;font-size:10.3px;line-height:13.7px;color:#333}
.field{position:absolute;width:217px;height:30px;border:1px solid #c8c8c8;border-radius:4px;background:#fff;box-shadow:inset 0 1px 2px rgba(0,0,0,.12);font-family:"Signika",sans-serif;font-weight:300;font-size:13px;color:#333;line-height:28px;padding-left:8px;white-space:nowrap}
.field .caret{position:absolute;right:8px;top:11px}
.search-btn{position:absolute;left:15px;top:226px;height:30px;border-radius:4px;background:linear-gradient(#ff9a2b,var(--orange-deep));color:#fff;font-family:"Signika",sans-serif;font-weight:300;font-size:16px;line-height:30px;padding:0 9px 0 11px;display:flex;align-items:center;gap:6px;white-space:nowrap}

.carousel-arrow{position:absolute;top:395px;width:58px;height:58px;border-radius:50%;background:rgba(255,255,255,.35);border:2px solid rgba(255,255,255,.6)}
.carousel-arrow svg{position:absolute;left:19px;top:16px}

.service-card{position:absolute;top:341px;width:274px;height:171px;border:3px solid var(--blue);background:var(--blue)}
.service-card.loan{border-color:var(--orange);background:var(--orange)}
.service-card .visual{height:126px}
.service-card .label{height:42px;display:flex;align-items:baseline;justify-content:center;gap:6px;color:#fff;font-family:"Yanone Kaffeesatz",sans-serif;white-space:nowrap}
.service-card.loan .label{color:#1a1a1a}
.service-card .label small{font-weight:300;font-size:19px}
.service-card .label strong{font-weight:600;font-size:38px;line-height:42px}

.features{position:absolute;left:0;top:549px}
.feature{position:absolute;width:320px}
.feature .icon{position:absolute;left:0;top:4px;width:34px;height:34px;border-radius:6px}
.feature h3{position:absolute;left:41px;top:0;font-family:"Signika",sans-serif;font-weight:300;font-size:19px;color:#1d3450;white-space:nowrap}
.feature p{position:absolute;left:42px;top:24px;font-size:10.5px;color:#444;white-space:nowrap}
.divider{position:absolute;left:838px;top:553px;width:1px;height:90px;background:#cfd6dc}
.auth-name{position:absolute;left:860px;top:582px;display:flex;align-items:center;gap:6px;font-family:"Yanone Kaffeesatz",sans-serif;font-weight:600;font-size:22px;color:#1f5fb0;white-space:nowrap}
.auth-name .sq{width:10px;height:10px;background:#d8a21a;border-radius:50%}
.auth-alt{position:absolute;left:966px;top:568px;width:42px;height:43px;border-radius:7px;background:linear-gradient(#4d83d0,#1c4f9c)}

/* footer */
.site-footer{position:absolute;left:0;top:814px;width:1200px;height:157px;background:var(--footer)}
.footer-brand{position:absolute;left:216px;top:35px;width:145px;text-align:center}
.footer-brand .brand-mark{margin:0 auto 8px;width:46px;height:46px;background:var(--brand-blue)}
.footer-brand .brand-name{font-size:19px;color:#e8e8e8;letter-spacing:.5px}
.footer-col{position:absolute;top:28px;color:#e6e6e6;font-size:10.5px;line-height:15.5px}
.footer-col h4{font-family:"Signika",sans-serif;font-weight:400;font-size:15px;color:var(--gold);margin-bottom:14px;white-space:nowrap}
.footer-col b{color:#fff}
.pay-badges{display:flex;gap:8px;margin-top:8px}
.pay-badges i{display:block;width:30px;height:20px;border-radius:2px;background:#d8d8d8}
.pay-badges i:nth-child(1){background:#e9a15a}
.pay-badges i:nth-child(2){background:#2b63b0}
.pay-badges i:nth-child(3){background:#efd98a}

.footer-bar{position:absolute;left:0;top:971px;width:1200px;height:58px;background:var(--footer-bar);border-top:1px solid #3a3a3a}
.footer-links{position:absolute;left:200px;top:24px;font-size:10px;color:#e0e0e0;display:flex;gap:6px;white-space:nowrap}
.footer-links span.bar{color:#bbb}
.footer-social{position:absolute;left:879px;top:12px;display:flex;gap:6px}
.footer-social i{display:block;width:20px;height:20px;border-radius:50%;background:#555}
.copyright{position:absolute;right:195px;top:40px;font-size:9.5px;color:#8a8a8a;white-space:nowrap}
</style>
</head>
<body>

<header class="site-header">
  <div class="brand">
    <div class="brand-mark"></div>
    <div class="brand-name">LEDGER NEST</div>
  </div>
  <div class="account">
    <span class="register">REGISTRATION</span>
    <span class="sign-in">SIGN IN</span>
  </div>
  <div class="social-connect"><span class="sq"></span>Connect with Kindlebook</div>
  <div class="header-social"><i></i><i></i><i></i><i></i></div>
</header>

<nav class="main-nav">
  <a class="active" style="left:215px">HOMEPAGE</a>
  <a style="left:317px">ABOUT US</a><span class="sep" style="left:391px"></span>
  <a style="left:418px">LOAN</a><span class="sep" style="left:470px"></span>
  <a style="left:489px">CREATE &nbsp;A PAYMENT PLAN</a><span class="sep" style="left:651px"></span>
  <a style="left:669px">MAKE A PAYMENT</a><span class="sep" style="left:787px"></span>
  <a style="left:804px">LEARN MORE</a><span class="sep" style="left:902px"></span>
  <a style="left:921px">CONTACT US</a>
</nav>

<section class="hero">
  <div class="hero-city" role="img" aria-label="Isometric city illustration with buildings, roads, cars, a market and green parkland"></div>

  <form class="search-panel">
    <div class="eyebrow">Search your place for loan</div>
    <h1>Easy Loan Process</h1>
    <p>Lorem ipsum dolor sit amet, consectetur adipisicing elit, sed do eiusmod tempor incididunt ut labore et dolore magna aliqua. Ut enim ad minim veniam, quis nostrud exercitation ullamco laboris nisi ut aliquip ex ea commodo consequat.</p>
    <div class="field" style="left:12px;top:141px">Choose your Option
      <svg class="caret" width="9" height="8" viewBox="0 0 9 8"><path d="M0 0h9L4.5 8z" fill="#333"/></svg></div>
    <div class="field" style="left:240px;top:141px">Country</div>
    <div class="field" style="left:12px;top:178px">City</div>
    <div class="field" style="left:240px;top:178px">ZipCode</div>
    <div class="search-btn">Search for Loan
      <svg width="16" height="16" viewBox="0 0 16 16"><circle cx="8" cy="8" r="7" fill="none" stroke="#fff" stroke-width="1.6"/><path d="M6.5 4.5L10 8l-3.5 3.5" fill="none" stroke="#fff" stroke-width="1.8"/></svg></div>
  </form>

  <div class="carousel-arrow" style="left:105px"><svg width="18" height="24" viewBox="0 0 18 24"><path d="M14 1L3 12l11 11" fill="none" stroke="#b9c6d0" stroke-width="2"/></svg></div>
  <div class="carousel-arrow" style="left:1035px"><svg width="18" height="24" viewBox="0 0 18 24"><path d="M4 1l11 11L4 23" fill="none" stroke="#b9c6d0" stroke-width="2"/></svg></div>

  <div class="service-card loan" style="left:175px">
    <div class="visual" role="img" aria-label="Large green plus sign resting on a stack of banknotes" style="background:linear-gradient(135deg,#f4f4f4 0%,#e9f3e2 45%,#5fbf2a 60%,#d9dcd4 100%)"></div>
    <div class="label"><small>SEARCH FOR A</small><strong>LOAN</strong></div>
  </div>
  <div class="service-card" style="left:463px">
    <div class="visual" role="img" aria-label="Close-up of individual income tax return forms" style="background:linear-gradient(120deg,#f2f2f2 0%,#dcdcdc 50%,#f7f7f7 100%)"></div>
    <div class="label"><small>CREATE A</small><strong>PAYMENT PLAN</strong></div>
  </div>
  <div class="service-card" style="left:751px">
    <div class="visual" role="img" aria-label="Fanned stacks of hundred dollar banknotes" style="background:linear-gradient(120deg,#efefef 0%,#b9b9b9 45%,#e4e4e4 100%)"></div>
    <div class="label"><small>MAKE A</small><strong>PAYMENT</strong></div>
  </div>

  <div class="features">
    <div class="feature" style="left:182px;top:14px">
      <div class="icon" role="img" aria-label="Business person icon" style="background:#9aa8b4"></div>
      <h3>Healthcare Loans</h3><p>Lorem ipsum dolor sit amet, consectetur adipisicing elit,</p></div>
    <div class="feature" style="left:500px;top:14px">
      <div class="icon" role="img" aria-label="Market building icon" style="background:#b7c2a8"></div>
      <h3>Medical Market</h3><p>Lorem ipsum dolor sit amet, consectetur adipisicing elit,</p></div>
    <div class="feature" style="left:182px;top:67px">
      <div class="icon" role="img" aria-label="Finance chart with coins icon" style="background:#c5c98a"></div>
      <h3>Financial Suite</h3><p>Lorem ipsum dolor sit amet, consectetur adipisicing elit,</p></div>
    <div class="feature" style="left:500px;top:67px">
      <svg class="icon" width="34" height="34" viewBox="0 0 34 34" aria-hidden="true"><circle cx="17" cy="17" r="15" fill="#fff" stroke="#d62c2c" stroke-width="3"/><path d="M14 8h6v6h6v6h-6v6h-6v-6H8v-6h6z" fill="#e23b3b"/></svg>
      <h3>Fast Setup</h3><p>Lorem ipsum dolor sit amet, consectetur adipisicing elit,</p></div>
  </div>
  <div class="divider"></div>
  <div class="auth-name"><span class="sq"></span>TrellisKey</div>
  <div class="auth-alt" role="img" aria-label="Alternative sign-in option"></div>
</section>

<footer class="site-footer">
  <div class="footer-brand">
    <div class="brand-mark"></div>
    <div class="brand-name">LEDGER NEST</div>
  </div>
  <div class="footer-col" style="left:414px;width:250px">
    <h4>Payment method</h4>
    <b>Ma quande lingues coalesce, li grammatica del resultant lingue es plu</b> simplic e regulari quam ti del coalescent lingues. Li nov lingua franca va esser plu simplic e regulari quam li existent Europan lingues.
    <div class="pay-badges"><i></i><i></i><i></i></div>
  </div>
  <div class="footer-col" style="left:687px;width:180px">
    <h4>Get in touch</h4>
    <b>218 Orchard Lane #5</b><br>Ashford, CA, 94512<br><b>Phone:</b> (555) 014-2290 ext#1<br><b>FAX:</b> (555) 014-2291<br><b>Email:</b> info@ledgernest.example
  </div>
  <div class="footer-col" style="left:893px;width:125px">
    <h4>Ledger Nest details</h4>
    Lorem ipsum dolor sit amet, consectetuer adipi-scing elit, sed diam nonummy nibh euismod tincidunt ut laoreet dolore
  </div>
</footer>

<div class="footer-bar">
  <div class="footer-links">
    <span>Homepage</span><span class="bar">|</span><span>About Us</span><span class="bar">|</span><span>Loan</span><span class="bar">|</span><span>Create a Payment Plan</span><span class="bar">|</span><span>Make a Payment</span><span class="bar">|</span><span>Learn More</span><span class="bar">|</span><span>Contact Us</span>
  </div>
  <div class="footer-social"><i></i><i></i><i></i><i></i><i></i></div>
  <div class="copyright">Copyright © 2012 LedgerNest. All rights reserved.</div>
</div>

</body>
</html>
```